Geschäftspapiere für Spezialist für Fliesen, Kaminöfen etc.
Zielgruppe
Wir sind ein Familienunternehmen in dritter Generation und Spezialist für Fliesen, Natursteine, Kaminöfen, Schwimmbäder und Whirlpools. Professionell, kreativ und voller Leidenschaft begleiten wir unsere Kunden bei der Umsetzung ihrer Vorhaben. Von der persönlichen Beratung bis hin zur Ausführung profitieren unsere Kunden von qualifiziertem Fachpersonal und 60 Jahren Erfahrung. Unsere Zielgruppe sind Familien/Paare ab 35 Jahren, die hochwertige Produkte für Ihr Zuhause suchen.
Aufgabenstellung
Wir benötigen neues Briefpapier, da wir ein neues Logo haben. Wir hätten gerne drei bis vier Bilder in der Kopfleiste. Des weiteren soll unser Portfolio aufgelistet sein (Fliesen, Natursteine, Kaminöfen, Schwimmbäder und Whirlpools). Das Logo soll in weiß gedruckt werden, der Hintergrund sollte daher dunkel sein (Farbton ähnlich DB703). Wir haben bereits selbst einen Entwurf gestaltet, in welche Richtung das Design gehen soll, sind jedoch offen für Ideen und Vorschläge.
Schriftart: z. B. Syncopate in Großbuchstaben

```html
<!DOCTYPE html>
<html lang="de">
<head>
<meta charset="utf-8">
<title>Briefbogen Marmor-Keller GmbH</title>
<link rel="stylesheet" href="https://fonts.googleapis.com/css2?family=Questrial&display=swap">
<style>
  :root {
    --backdrop: #d0c8c8;
    --paper: #ffffff;
    --brand-dark: #464241;
    --ink: #2a2828;
    --rule: #6e6a6a;
    --bath-a: #eceeef; --bath-b: #d6d3cf;
    --fire-a: #b9a58e; --fire-b: #5b4a3e;
    --pool-a: #cfe3ee; --pool-b: #7fb04e;
  }
  * { margin: 0; padding: 0; box-sizing: border-box; }
  html, body { width: 960px; height: 1200px; overflow: hidden; background: var(--backdrop); }
  body { position: relative; font-family: "Questrial", sans-serif; color: var(--ink); }
  .sheet { position: absolute; left: 83px; top: 39px; width: 793px; height: 1121px; background: var(--paper); }
  .masthead { position: absolute; left: 0; top: 0; width: 793px; height: 117px; display: block; }
  .brand-name {
    position: absolute; left: 570px; top: 42px; width: 200px;
    font-size: 34px; letter-spacing: 11px; color: var(--paper); line-height: 1;
  }
  .portfolio {
    position: absolute; left: 48px; top: 130px; width: 698px;
    display: flex; justify-content: space-between;
    font-size: 16px; letter-spacing: 3.2px; text-transform: uppercase; color: var(--ink);
  }
  .return-address { position: absolute; left: 95px; top: 187px; font-size: 9.6px; letter-spacing: 0.2px; }
  .contact { position: absolute; left: 571px; top: 182px; font-size: 12.5px; line-height: 16px; letter-spacing: 0.3px; }
  .contact p + p { margin-top: 16px; }
  .fold-mark { position: absolute; left: 0; width: 10px; height: 1px; background: var(--ink); }
  .fold-mark.upper { top: 397px; }
  .fold-mark.lower { top: 559px; }
  .footer-rule { position: absolute; left: 0; top: 1044px; width: 793px; height: 1px; background: var(--rule); }
  .footer-col { position: absolute; top: 1052px; font-size: 11.5px; line-height: 14.5px; letter-spacing: 0.3px; }
  .footer-col.bank { left: 300px; }
  .footer-col.legal { left: 571px; }
  .footer-col .gap { display: inline-block; width: 22px; }
</style>
</head>
<body>
  <div class="sheet">
    <svg class="masthead" viewBox="0 0 793 117" xmlns="http://www.w3.org/2000/svg">
      <defs>
        <linearGradient id="bathTone" x1="0" y1="0" x2="1" y2="1">
          <stop offset="0" stop-color="var(--bath-a)"/><stop offset="1" stop-color="var(--bath-b)"/>
        </linearGradient>
        <linearGradient id="fireTone" x1="0" y1="0" x2="0" y2="1">
          <stop offset="0" stop-color="var(--fire-a)"/><stop offset="1" stop-color="var(--fire-b)"/>
        </linearGradient>
        <linearGradient id="poolTone" x1="0" y1="0" x2="0" y2="1">
          <stop offset="0" stop-color="var(--pool-a)"/><stop offset="1" stop-color="var(--pool-b)"/>
        </linearGradient>
      </defs>
      <rect width="793" height="117" fill="var(--brand-dark)"/>
      <polygon role="img" aria-label="Foto: helles Badezimmer mit Marmorfliesen und freistehender Wanne" points="0,0 196,0 172,117 0,117" fill="url(#bathTone)"/>
      <polygon role="img" aria-label="Foto: Wohnraum mit Kaminofen vor Natursteinwand" points="226,0 426,0 372,117 186,117" fill="url(#fireTone)"/>
      <polygon role="img" aria-label="Foto: moderne Villa mit Schwimmbad im Garten" points="428,0 612,0 572,117 386,117" fill="url(#poolTone)"/>
    </svg>
    <div class="brand-name">KELLER</div>

    <nav class="portfolio">
      <span>Fliesen</span><span>Natursteine</span><span>Kaminöfen</span><span>Schwimmbäder</span><span>Whirlpools</span>
    </nav>

    <div class="return-address">Marmor-Keller GmbH&nbsp; Lindenweg 12&nbsp; 76829 Landau</div>

    <address class="contact" style="font-style:normal">
      <p>Marmor-Keller GmbH<br>Lindenweg 12<br>76829 Landau</p>
      <p>Tel.: +49 6341 482200<br>info@marmor-keller.de</p>
    </address>

    <div class="fold-mark upper"></div>
    <div class="fold-mark lower"></div>

    <div class="footer-rule"></div>
    <div class="footer-col bank">
      Kontoverbindung<br>
      &nbsp;IBAN: DE00 1111 2222 3333 4444 55<br>
      BLZ:<span class="gap"></span>000&nbsp; 000&nbsp; 000
    </div>
    <div class="footer-col legal">
      Gerichtsstand xxxxxxxxx<br>
      Steuer-Nr. 111/222/00000<br>
      Finanzamt XYZXYZXYZ
    </div>
  </div>
</body>
</html>
```